Thank you cards for online orders

We have a logo that is attached and I'd for it to be used to make a thank you card that will give our clients some info on product care as well as refund/exchange policy. so maybe a small package that includes a thank you card, and policy details
Updates

Sick

Target Market(s)

Females for 20-70

```html
<!DOCTYPE html>
<html lang="en">
<head>
<meta charset="utf-8">
<title>Velora – Thank You Card</title>
<link rel="stylesheet" href="https://fonts.googleapis.com/css2?family=Raleway:wght@300;400;500;700&family=Cinzel:wght@400&display=swap">
<style>
  :root {
    --paper: #efeded;
    --green: #62a833;
    --teal: #1c8f96;
    --white: #ffffff;
    --skin-light: #e2b39b;
    --skin-warm: #c98f72;
    --skin-deep: #8a5a45;
    --hair: #3b2a26;
    --blush: #eccbd0;
    --gold: #c7a15e;
    --silver: #cfd3d8;
    --red: #c63a3e;
  }
  * { margin: 0; padding: 0; box-sizing: border-box; }
  html, body { width: 849px; height: 1200px; overflow: hidden; background: var(--paper); }
  .card {
    position: relative;
    width: 849px;
    height: 1200px;
    background: var(--paper);
    font-family: "Raleway", sans-serif;
  }
  .pennant { position: absolute; left: 0; top: 0; width: 849px; height: 370px; }
  .brand {
    position: absolute;
    top: 40px; left: 0; width: 849px;
    text-align: center;
    color: var(--white);
    font-weight: 300;
    font-size: 46px;
    letter-spacing: 7px;
  }
  .established {
    position: absolute;
    top: 96px; left: 0; width: 849px;
    text-align: center;
    color: var(--white);
    font-family: "Cinzel", serif;
    font-size: 13px;
    letter-spacing: 2px;
  }
  .headline {
    position: absolute;
    top: 134px; left: 0; width: 849px;
    text-align: center;
    color: var(--white);
    font-weight: 700;
    font-size: 50px;
    letter-spacing: 3px;
  }
  .photo {
    position: absolute;
    width: 214px; height: 214px;
    border-radius: 50%;
  }
  .photo--teal { box-shadow: 7px -5px 0 0 var(--teal); }
  .photo--green { box-shadow: -7px -5px 0 0 var(--green); }
  .photo-1 { left: 44px;  top: 452px; background: linear-gradient(180deg, var(--skin-light) 0%, var(--skin-warm) 45%, var(--gold) 62%, var(--skin-light) 100%); }
  .photo-2 { left: 311px; top: 452px; background: linear-gradient(160deg, var(--skin-deep) 0%, #a87460 45%, var(--gold) 70%, #d9b7b4 100%); }
  .photo-3 { left: 583px; top: 452px; background: linear-gradient(180deg, var(--blush) 0%, var(--blush) 30%, #e6d7bf 55%, var(--silver) 100%); }
  .photo-4 { left: 160px; top: 724px; background: linear-gradient(150deg, var(--hair) 0%, var(--skin-deep) 40%, #d8cba8 70%, var(--silver) 100%); }
  .photo-5 { left: 454px; top: 724px; background: linear-gradient(180deg, var(--blush) 0%, var(--skin-warm) 40%, #a7b99a 65%, var(--red) 100%); }
  .section-title {
    position: absolute;
    left: 36px; top: 994px;
    color: var(--green);
    font-weight: 400;
    font-size: 38px;
    letter-spacing: 2px;
  }
  .rule {
    position: absolute;
    left: 0; top: 1045px;
    width: 849px; height: 9px;
    background: var(--green);
  }
  .info-band {
    position: absolute;
    left: 0; top: 1069px;
    width: 849px; height: 131px;
    background: var(--green);
    color: var(--white);
    text-align: center;
    font-weight: 500;
    font-size: 20px;
    line-height: 24px;
    letter-spacing: 0.6px;
    padding: 29px 34px 0;
  }
</style>
</head>
<body>
<main class="card">
  <svg class="pennant" viewBox="0 0 849 370" aria-hidden="true">
    <polygon points="88,0 761,0 761,186 424,352 88,186" fill="var(--green)"/>
    <polyline points="88,0 88,186 424,352 761,186 761,0" fill="none" stroke="var(--green)" stroke-width="6"/>
    <polyline points="97,0 97,181 424,342 752,181 752,0" fill="none" stroke="var(--white)" stroke-width="5"/>
  </svg>
  <div class="brand">VELORA</div>
  <div class="established">EST. 2006</div>
  <h1 class="headline">THANK YOU</h1>

  <div class="photo photo--teal photo-1" role="img" aria-label="Close-up of a model wearing a gold and turquoise choker necklace"></div>
  <div class="photo photo--teal photo-2" role="img" aria-label="Model wearing a gold kundan necklace with matching earrings"></div>
  <div class="photo photo--teal photo-3" role="img" aria-label="Pearl and gold choker shown with pink roses"></div>
  <div class="photo photo--green photo-4" role="img" aria-label="Model with dark hair wearing a layered gold necklace"></div>
  <div class="photo photo--green photo-5" role="img" aria-label="Model in a red outfit wearing a green and gold necklace"></div>

  <h2 class="section-title">About the Product</h2>
  <div class="rule"></div>
  <p class="info-band">Keep your jewellery in its pouch, away from water, perfume and lotion, and wipe it with a soft dry cloth. Returns and exchanges are accepted within 7 days in original packaging.</p>
</main>
</body>
</html>
```